Letterhead and email signiture

Hello,

I have an example of a letterhead that we need. The one we have constandly moves if we paste any information in it. We are looking for one that is permanent. We only need the top of the letterhead on the first page but the bottom on each and every page afterward.

It does not have to be exactly what I am providing here. Please take a look at the website and maybe you will have a better idea.

We are looking to do something similar for an email signature

Marvistoinc.com

```html
<!DOCTYPE html>
<html lang="en">
<head>
<meta charset="utf-8">
<title>Marvisto Inc – Letterhead and Business Card</title>
<link rel="stylesheet" href="https://fonts.googleapis.com/css2?family=Arimo:wght@400&family=Roboto:wght@400;500;700&family=Roboto+Condensed:wght@300&display=swap">
<style>
  :root {
    --backdrop: #bcbcbc;
    --paper: #ffffff;
    --ink: #1a1a1a;
    --text: #4a4a4a;
    --muted: #555555;
    --rule: #8a8a8a;
    --accent: #3d8bd4;
  }
  * { box-sizing: border-box; margin: 0; padding: 0; }
  html, body { width: 884px; height: 1200px; overflow: hidden; }
  body { background: var(--backdrop); position: relative; font-family: "Arimo", Arial, sans-serif; }

  .letterhead {
    position: absolute; left: 160px; top: 42px; width: 565px; height: 799px;
    background: var(--paper); box-shadow: 2px 3px 5px rgba(0,0,0,.35);
    overflow: hidden;
  }
  .letterhead__masthead {
    position: absolute; left: 84px; top: 71px; width: 396px; height: 26px;
    display: flex; align-items: center; gap: 6px;
  }
  .letterhead__masthead .rule { flex: 1; height: 1px; background: var(--rule); }
  .wordmark {
    font-family: "Roboto", Arial, sans-serif; font-weight: 700; color: var(--ink);
    letter-spacing: -0.3px; white-space: nowrap;
  }
  .letterhead .wordmark { font-size: 19px; }

  .letter { position: absolute; left: 50px; top: 245px; width: 463px; color: var(--text); }
  .letter__salutation { font-size: 12px; margin-left: 1px; margin-bottom: 21px; }
  .letter__body p { font-size: 9.55px; line-height: 11.7px; margin-bottom: 10px; }
  .letter__closing { font-size: 7.5px; margin-top: 20px; margin-left: 1px; }
  .letter__signature {
    font-family: "Roboto Condensed", Arial, sans-serif; font-weight: 300;
    font-size: 14px; letter-spacing: -0.6px; color: var(--muted); margin-top: 20px; margin-left: -9px;
  }

  .letterhead__footer { position: absolute; left: 84px; top: 747px; width: 396px; text-align: center; color: var(--text); }
  .contact-row {
    display: flex; justify-content: center; align-items: center; gap: 6px;
    font-size: 8.6px; line-height: 11px; padding-bottom: 3px; border-bottom: 1px solid var(--rule);
  }
  .contact-row span { display: inline-flex; align-items: center; gap: 2px; }
  .icon { fill: var(--accent); flex: none; }
  .disclaimer { font-size: 8.8px; line-height: 11px; margin-top: 4px; white-space: nowrap; margin-left: -2px; margin-right: -2px; }

  .business-card {
    position: absolute; left: 139px; top: 879px; width: 607px; height: 242px;
    background: var(--paper); box-shadow: 2px 3px 5px rgba(0,0,0,.35);
    font-family: "Roboto", Arial, sans-serif;
  }
  .business-card .wordmark { position: absolute; left: 30px; top: 79px; font-size: 30px; }
  .business-card__divider { position: absolute; left: 303px; top: 40px; width: 1px; height: 116px; background: var(--rule); }
  .holder { position: absolute; left: 319px; top: 38px; color: var(--muted); }
  .holder__name { font-size: 20.5px; font-weight: 500; color: var(--accent); line-height: 24px; }
  .holder__title { font-size: 15.5px; line-height: 18px; }
  .holder__contacts { list-style: none; margin-top: 16px; font-size: 17px; line-height: 20.5px; }
  .holder__contacts li { display: flex; align-items: center; gap: 5px; }
  .business-card__rule { position: absolute; left: 27px; top: 174px; width: 553px; height: 1px; background: var(--rule); }
  .business-card__disclaimer { position: absolute; left: 0; top: 183px; width: 100%; text-align: center; font-size: 16.5px; line-height: 21px; color: var(--muted); }
</style>
</head>
<body>

<section class="letterhead">
  <header class="letterhead__masthead">
    <span class="rule"></span>
    <span class="wordmark">MARVISTO INC</span>
    <span class="rule"></span>
  </header>

  <article class="letter">
    <p class="letter__salutation">Dear Mr. Brooks,</p>
    <div class="letter__body">
      <p>Lorem ipsum dolor sit amet, consectetuer adipiscing elit, sed diam nonmmy nibh euismod tincidunt ut laor eet dolore magna aliquam erat volutpat. Ut wisi enim ad minim veniam, quis nostrud exerci tationmcorper suscipit lobortis nisl ut aliquip ex ea commodo consequat. Duis autem vel eum iriure dolor in hendrerit in vulputate velit esse molestie consequat, vel illum dolore eu feugiat</p>
      <p>Rorem ipsum dolor sit amet, consectetuer adipiscing elit, sed diam nonmmy nibh euismod tincidunt ut laor eet dolore magna aliquam erat volutpat. Ut wisi enim ad minim veniam, quis nostrud exerci tationmcorper suscipit lobortis nisl ut aliquip ex ea commodo consequat. Duis autem vel eum iriure dolor in hendrerit in vulputate velit esse molest</p>
      <p>Dorem ipsum dolor sit amet, consectetuer adipiscing elit, sed diam nonmmy nibh euismod tincidunt ut laor eet dolore magna aliquam erat volutpat. Ut wisi enim ad minim veniam, quis nostrud exerci tationmcorper suscipit lobortis nisl ut aliquip ex ea commodo consequat. Duis autem vel eum iriure dolor in hendrerit in suscipit lobortis nisl ut aliquip ex ea commodo consequat. Duis autem vel eum iriure dolor in hendrerit in vulputate velit esse molestie consequat, vel illum</p>
      <p>Sorem ipsum dolor sit amet, consectetuer adipiscing elit, sed diam nonmmy nibh euismod tincidunt ut laor eet dolore magna aliquam erat volutpat. Ut wisi enim ad minim veniam, quis nostrud exerci tationmcorper suscipit lobortis nisl ut aliquip ex ea commodo consequat. Duis autem vel eum iriure dolor in</p>
    </div>
    <p class="letter__closing">Sincerely,</p>
    <p class="letter__signature">Martin Halloway</p>
  </article>

  <footer class="letterhead__footer">
    <div class="contact-row">
      <span><svg class="icon" width="8" height="7" viewBox="0 0 16 14"><path d="M1 5c0-3 14-3 14 0v1h-4V4H5v2H1zM4 7h8l3 6H1z"/></svg>305-555-0142</span>
      <span><svg class="icon" width="8" height="7" viewBox="0 0 16 14"><path d="M1 5c0-3 14-3 14 0v1h-4V4H5v2H1zM4 7h8l3 6H1z"/></svg>&nbsp;904-555-0187</span>
      <span><svg class="icon" width="8" height="8" viewBox="0 0 16 16"><circle cx="8" cy="8" r="7.5"/></svg>&nbsp;MARVISTOINC.COM</span>
    </div>
    <p class="disclaimer">This document is confidential and intended solely for investigative purposes by Marvisto Inc.</p>
  </footer>
</section>

<section class="business-card">
  <span class="wordmark">MARVISTO INC</span>
  <span class="business-card__divider"></span>
  <div class="holder">
    <p class="holder__name">DANIEL BROOKS</p>
    <p class="holder__title">Manager</p>
    <ul class="holder__contacts">
      <li><svg class="icon" width="15" height="13" viewBox="0 0 16 14"><path d="M1 5c0-3 14-3 14 0v1h-4V4H5v2H1zM4 7h8l3 6H1z"/></svg>305-555-0142</li>
      <li><svg class="icon" width="15" height="13" viewBox="0 0 16 14"><path d="M1 5c0-3 14-3 14 0v1h-4V4H5v2H1zM4 7h8l3 6H1z"/></svg>904-555-0187</li>
      <li><svg class="icon" width="15" height="15" viewBox="0 0 16 16"><circle cx="8" cy="8" r="7.5"/></svg>MARVISTOINC.COM</li>
    </ul>
  </div>
  <span class="business-card__rule"></span>
  <p class="business-card__disclaimer">This document is confidential and<br>intended solely for investigative purposes by Marvisto Inc.</p>
</section>

</body>
</html>
```